Business cards for a naturopathic day clinic for stem cell therapy

We need a basic design for a day clinic, that offers stem cell therapies for Lyme therapy and other severe chronic illnesses.
Our name is "Casa velorìn", which can be translated into "Manor Velorbloom". We are a couple of naturopaths working along side physiotherapists and osteopaths, yoga teachers and massage therapists. I attached our logo.

```html
<!DOCTYPE html>
<html lang="en">
<head>
<meta charset="utf-8">
<title>Casa velorìn – Business Cards</title>
<link rel="stylesheet" href="https://fonts.googleapis.com/css2?family=Mulish:wght@300;400;600&display=swap">
<style>
  :root {
    --backdrop: #9b9b9b;
    --paper: #f7f7f5;
    --taupe: #8c7766;
    --taupe-line: #9c8a7c;
    --leaf: #a9c24b;
    --ink: #5a5a5a;
    --white: #ffffff;
  }
  * { margin: 0; padding: 0; box-sizing: border-box; }
  html, body { width: 1200px; height: 1050px; overflow: hidden; }
  body {
    background: var(--backdrop);
    font-family: "Mulish", sans-serif;
    position: relative;
  }
  .card { position: absolute; box-shadow: 0 18px 40px rgba(0,0,0,0.25); }

  /* Front card, portrait */
  .card-front {
    left: 90px; top: 165px;
    width: 400px; height: 720px;
    background: var(--paper);
    display: flex; flex-direction: column; align-items: center;
    padding-top: 90px;
    text-align: center;
  }
  .brand-mark {
    display: flex; align-items: center; gap: 14px;
    color: var(--leaf);
    font-size: 30px; font-weight: 400;
    margin-bottom: 70px;
  }
  .brand-dot {
    width: 22px; height: 22px; border-radius: 50%;
    background: var(--leaf);
  }
  .person-name {
    color: var(--leaf);
    font-size: 26px; font-weight: 400;
    letter-spacing: 1px;
    text-transform: uppercase;
  }
  .person-role {
    color: var(--taupe-line);
    font-size: 17px; font-weight: 400;
    margin-top: 2px;
  }
  .divider {
    width: 22px; height: 2px;
    background: var(--leaf);
    margin: 26px 0 26px;
  }
  .address {
    color: var(--ink);
    font-size: 17px; font-weight: 300;
    line-height: 1.45;
  }
  .icon-row {
    display: flex; gap: 10px;
    margin: 26px 0 28px;
  }
  .icon-row svg { width: 30px; height: 30px; }
  .contact-list {
    list-style: none;
    color: var(--ink);
    font-size: 17px; font-weight: 300;
    line-height: 1.45;
  }

  /* Back card, landscape */
  .card-back {
    left: 540px; top: 500px;
    width: 600px; height: 343px;
    background: var(--taupe);
    display: flex; align-items: center; justify-content: center;
    gap: 22px;
  }
  .back-dot {
    width: 58px; height: 58px; border-radius: 50%;
    background: var(--leaf);
  }
  .back-name {
    color: var(--white);
    font-size: 62px; font-weight: 300;
    letter-spacing: 0.5px;
  }
</style>
</head>
<body>

<section class="card card-front">
  <div class="brand-mark"><span class="brand-dot"></span>Casa velorìn</div>

  <h1 class="person-name">Elias Moreno</h1>
  <p class="person-role">President</p>
  <span class="divider"></span>

  <p class="address">1204 Fernhill Road<br>Juneau, Alaska 99801</p>

  <div class="icon-row">
    <svg viewBox="0 0 30 30" aria-label="Phone">
      <circle cx="15" cy="15" r="13.5" fill="none" stroke="var(--taupe-line)" stroke-width="2"/>
      <path d="M10 9.5c1-.8 2 .2 2.6 1.3.4.8-.2 1.3-.6 1.8.7 1.6 1.8 2.8 3.4 3.5.5-.4 1-1 1.8-.6 1.1.6 2.1 1.6 1.3 2.6-1 1.3-2.6 1.2-4.2.3-2.2-1.2-3.7-2.8-4.8-5-.7-1.5-.8-3 .5-3.9z" fill="var(--leaf)"/>
    </svg>
    <svg viewBox="0 0 30 30" aria-label="Mobile">
      <circle cx="15" cy="15" r="13.5" fill="none" stroke="var(--taupe-line)" stroke-width="2"/>
      <rect x="11" y="8" width="8" height="14" rx="1.2" fill="none" stroke="var(--leaf)" stroke-width="1.6"/>
    </svg>
    <svg viewBox="0 0 30 30" aria-label="Fax">
      <circle cx="15" cy="15" r="13.5" fill="none" stroke="var(--taupe-line)" stroke-width="2"/>
      <rect x="11" y="8" width="8" height="5" fill="var(--leaf)"/>
      <rect x="8.5" y="13" width="13" height="7" rx="1" fill="var(--leaf)"/>
      <rect x="11" y="18" width="8" height="4" fill="var(--paper)" stroke="var(--leaf)" stroke-width="1"/>
    </svg>
    <svg viewBox="0 0 30 30" aria-label="Email">
      <circle cx="15" cy="15" r="13.5" fill="none" stroke="var(--taupe-line)" stroke-width="2"/>
      <rect x="8.5" y="10.5" width="13" height="9" fill="var(--leaf)"/>
      <path d="M8.5 10.5l6.5 5 6.5-5" fill="none" stroke="var(--paper)" stroke-width="1.2"/>
    </svg>
    <svg viewBox="0 0 30 30" aria-label="Website">
      <circle cx="15" cy="15" r="13.5" fill="none" stroke="var(--taupe-line)" stroke-width="2"/>
      <circle cx="15" cy="15" r="6.5" fill="var(--leaf)"/>
      <path d="M8.5 15h13M15 8.5c-2.5 3.5-2.5 9.5 0 13M15 8.5c2.5 3.5 2.5 9.5 0 13" fill="none" stroke="var(--paper)" stroke-width="0.9"/>
    </svg>
  </div>

  <ul class="contact-list">
    <li>555-214-7730</li>
    <li>555-318-4926</li>
    <li>555-407-1583</li>
    <li>info@casavelorin.com</li>
    <li>casavelorin.com</li>
  </ul>
</section>

<section class="card card-back">
  <span class="back-dot"></span>
  <span class="back-name">Casa velorìn</span>
</section>

</body>
</html>
```